Web Design for couples website

About us:
Duoglimmer.sg is a new startup website that aims to suggest and promote activities for young couples. The site will feature a blog and a group deals page (i.e Bulkaro).

What we need:
We require a talented designer to design a theme for the website. The design must include at least the following:
1. Logo Design - A logo should be provided along with the website design. The design should match the overall design of the website (or vice versa). The logo should include the words "Duoglimmer.sg" or "Duoglimmer". Capitalisation of the alphabets are not critical.

2 - Home / Landing page
The layout of this page should be similar to the standard 2 / 3 column quillpress pages with an image slider on top to feature articles / deals. There should also be a column on the side to include widgets such as social networking and mailing list subscription, etc

3. Deals Listing Page
This page will have a listing of all current group deals, similar to that of Bulkaro. The layout can either have deals listed in 1 or 2 columns.

4. Past Deals Page - See references below

5. Deal Page
Detailed information page for each specific deal. This should include deal image, title, buy button, timer, social media buttons, two column text.

References for deal pages:
www.ventopik.com.sg
http://www.plumvoucher.com.au/daily-offers
www.tarnibuyasia.com
www.frolmart.com

6. General page design for miscellaneous pages like "About", "Contact", etc.

The overall theme of the website should cater to an audience of 18-30 year old young adults. Preferably to have something less colourful and give the overall feel of class. This should cater generally to females but males as well, so less (or no)pink / red would be preferable. But don't let yourself get restricted by these requirements and feel free to let your creative juices flow!
Updates

Hi Designers,

Thank you for your submissions so far. I would like to point out that the deal listing page will only be a sub section of the page.  Would appreciate if priority was given to the main / landing page slider and 2 or 3 columns for articles below.

Other priority would be for the single deal design, where I'm more interested to have more unique buttons such as "buy now" and "time left" .

Also to note, only .PSD design file is required. No coding (HTML / CSS) is necessary and should also be friendly for developers to work with.

Hi Designers,

 
Please submit proposal designs based on requirements on landing page or deal listings page as these would be my main requirements for consideration.

Also, Do try to keep the theme clean and easy on the eyes. Overall, I'm looking for something that is simplistic and/or classy with elegance.

Target Market(s)

18 - 30 years old young adults interested in dating and activities for couples

Industry/Entity Type

Media

Requirements
Must have
• - Logo
- Home
- Deal Page (specific)
- General layout

```html
<!DOCTYPE html>
<html lang="en">
<head>
<meta charset="utf-8">
<title>Duoglimmer – Activities Deals</title>
<link href="https://fonts.googleapis.com/css2?family=Arimo:wght@400;700&display=swap" rel="stylesheet">
<style>
:root{
  --sky-top:#cfeefa;
  --sky-bottom:#eaf8fd;
  --nav-dark:#2b2b2b;
  --nav-darker:#1c1c1c;
  --blue:#1fa3dc;
  --blue-dark:#0d84bf;
  --blue-light:#5cc6f1;
  --orange:#ff7a00;
  --orange-light:#ffa030;
  --text:#222;
  --muted:#666;
  --grey-card:#f2f2f2;
  --line:#dedede;
  --footer:#ececec;
  --bottom:#333;
}
*{box-sizing:border-box;margin:0;padding:0}
html,body{width:1200px;height:2472px;overflow:hidden}
body{font-family:"Arimo",Arial,sans-serif;color:var(--text);background:#fff;position:relative;font-size:14px}
.wrap{position:absolute;left:127px;width:946px}

/* header */
.masthead{position:absolute;top:0;left:0;width:1200px;height:147px;
  background:radial-gradient(ellipse at 55% 0%,#ffffff 0%,var(--sky-bottom) 35%,var(--sky-top) 100%)}
.brand{position:absolute;left:127px;top:44px}
.brand-row{display:flex;align-items:center;gap:8px}
.brand-mark{width:30px;height:30px;background:var(--orange);border-radius:3px}
.brand-name{font-size:38px;font-weight:700;color:var(--blue);letter-spacing:-1px;line-height:1}
.brand-tag{font-size:13px;font-weight:700;color:#1a1a1a;margin-top:4px;letter-spacing:.3px}
.city{position:absolute;left:451px;top:48px}
.city-name{font-size:21px;font-weight:700;color:#111;display:flex;align-items:center;gap:8px}
.city-sub{font-size:13px;color:#222;margin-top:6px}
.city-note{position:absolute;left:634px;top:44px;width:138px;height:58px;border-radius:4px;
  background:linear-gradient(135deg,rgba(40,60,70,.10),rgba(40,60,70,.18))}
.newsletter{position:absolute;left:821px;top:48px;width:252px}
.newsletter-title{font-size:13px;color:#111;margin-bottom:6px}
.newsletter-form{display:flex;height:27px}
.newsletter-input{flex:1;background:#fff;border:1px solid #b8d9e6;border-radius:4px 0 0 4px;font-size:11px;color:#555;padding:7px 8px}
.newsletter-send{width:62px;background:linear-gradient(var(--orange-light),var(--orange));color:#fff;font-weight:700;font-size:12px;display:flex;align-items:center;justify-content:center;border-radius:0 4px 4px 0}

/* nav */
.navbar{position:absolute;top:147px;left:0;width:1200px;height:50px;
  background:linear-gradient(var(--nav-dark),var(--nav-darker));border-bottom:4px solid var(--blue)}
.nav-main{position:absolute;left:127px;top:0;height:46px;font-size:13px;font-weight:700;color:#fff}
.nav-main a{position:absolute;white-space:nowrap;top:16px}
.nav-main .active::after{content:"";position:absolute;left:50%;top:26px;margin-left:-7px;border:7px solid transparent;border-top-color:#fff;border-bottom:0}
.nav-util{position:absolute;left:800px;top:13px;display:flex;align-items:center;font-size:11px;color:#fff;height:22px}
.sign-in{background:#fff;color:var(--blue);padding:4px 14px;clip-path:polygon(6px 0,100% 0,100% 100%,0 100%);font-weight:700}
.nav-util .sep{width:1px;height:20px;background:#777;margin:0 10px}
.social-circle{position:absolute;top:8px;width:30px;height:30px;border-radius:50%;background:#fff}

/* breadcrumb & search */
.breadcrumb{top:220px;font-size:10px;color:#111}
.search{top:252px;height:91px;border-radius:3px;background:linear-gradient(var(--blue-light),var(--blue-dark))}
.field{position:absolute;top:21px;height:30px;background:#fff;border:1px solid #9bd1e8;font-size:13px;color:#444;padding:7px 12px}
.field-hint{position:absolute;top:62px;font-size:10px;color:#fff}
.find-btn{position:absolute;left:797px;top:19px;width:142px;height:32px;background:linear-gradient(var(--orange-light),var(--orange));border-radius:4px;color:#fff;font-weight:700;font-size:16px;display:flex;align-items:center;justify-content:center}

/* content */
.page-title{top:378px;font-size:26px;font-weight:700;color:#111}
.page-intro{top:418px;width:680px;font-size:12px;line-height:17px;color:#444}
.sorter{top:492px;width:680px;height:30px;font-size:12px;color:#666}
.sorter b{position:absolute;left:0;top:7px;color:#111;font-size:14px}
.sorter span{position:absolute;top:8px}
.sorter .tab{left:122px;top:0;width:99px;height:29px;background:linear-gradient(var(--blue-light),var(--blue));color:#fff;display:flex;align-items:center;justify-content:center;border-radius:2px}
.sorter .tab::after{content:"";position:absolute;bottom:-7px;left:50%;margin-left:-7px;border:7px solid transparent;border-top-color:var(--blue);border-bottom:0}

.deals{top:545px;width:680px}
.deal{position:relative;height:247px;margin-bottom:17px;background:var(--grey-card);border-radius:3px;box-shadow:0 1px 3px rgba(0,0,0,.12)}
.deal.featured{background:#fff;border:2px solid #8fd3f0;box-shadow:0 1px 6px rgba(0,0,0,.18)}
.price-tag{position:absolute;left:-10px;top:26px;width:200px;height:57px;background:linear-gradient(var(--orange-light),var(--orange));
  clip-path:polygon(0 0,85% 0,100% 50%,85% 100%,0 100%);color:#fff;font-weight:700;display:flex;align-items:center;padding-left:48px;gap:6px}
.price-tag .amount{font-size:28px}
.price-tag .unit{font-size:19px}
.deal-title{position:absolute;left:207px;top:36px;width:440px;font-size:15px;line-height:18px;color:#111}
.deal.featured .deal-title{color:var(--blue)}
.stats{position:absolute;left:24px;top:101px;width:430px;font-size:13px}
.stat-row{position:relative;height:28px}
.stat-row.shaded{background:linear-gradient(90deg,#e2e2e2,#ececec 80%,transparent)}
.stat-row span{position:absolute;top:7px}
.c1{left:0}.c2{left:86px}.c3{left:149px}.c4{left:238px}
.orange{color:var(--orange)}
.icons{position:absolute;left:238px;top:7px;display:flex;gap:4px}
.icons i{width:14px;height:14px;border-radius:2px;display:block}
.btn{position:absolute;top:187px;height:26px;color:#fff;font-size:12px;display:flex;align-items:center;justify-content:center}
.btn-buy{left:19px;width:88px;background:linear-gradient(var(--blue-light),var(--blue));clip-path:polygon(0 0,100% 0,92% 100%,8% 100%)}
.btn-details{left:125px;width:76px;background:linear-gradient(var(--orange-light),var(--orange));clip-path:polygon(0 0,100% 0,92% 50%,100% 100%,0 100%,8% 50%)}
.deal-photo{position:absolute;left:471px;top:96px;width:190px;height:134px;border:5px solid #fff;box-shadow:0 1px 4px rgba(0,0,0,.3)}

/* sidebar */
.side{position:absolute;left:845px;width:228px}
.widget-head{height:29px;background:linear-gradient(var(--blue-light),var(--blue));color:#fff;font-size:15px;padding:6px 14px;position:relative}
.widget-head small{position:absolute;right:14px;top:7px;font-size:12px;text-decoration:underline}
.categories{top:370px;height:533px;background:var(--grey-card);border:1px solid var(--line)}
.categories ul{list-style:none;padding:5px 14px 0}
.categories li{height:34px;border-bottom:1px solid #dadada;font-size:12px;color:#555;padding-top:11px;padding-left:8px}
.categories li::before{content:"› ";color:#888}
.categories li.current{color:var(--blue);text-decoration:underline}
.fan-box{top:924px;height:256px;border:1px solid #ccc;background:#fff}
.fan-head{display:flex;gap:8px;padding:10px 8px;border-bottom:1px solid #ddd;height:60px}
.fan-mark{width:40px;height:40px;background:var(--blue);border-radius:3px}
.fan-name{font-size:11px;color:#3b5998}
.fan-name span{color:#333}
.like{margin-top:4px;width:38px;height:16px;border:1px solid #aaa;background:#eee;font-size:9px;text-align:center;line-height:14px}
.fan-count{font-size:10px;color:#333;padding:6px 8px}
.fans{display:grid;grid-template-columns:repeat(4,48px);gap:4px 6px;padding:0 8px}
.fan{font-size:8px;color:#555;text-align:center}
.fan div{height:46px;margin-bottom:2px}
.about{top:1204px}
.about h3{font-size:17px;color:#222;margin-bottom:6px}
.about p{font-size:12px;line-height:16px;color:#555;width:220px}

/* footer */
.footer{position:absolute;left:0;top:2168px;width:1200px;height:262px;background:var(--footer)}
.fcol{position:absolute;top:48px}
.fcol h4{font-size:15px;font-weight:400;color:var(--blue);margin-bottom:14px}
.fcol a{display:block;font-size:13px;color:#888;height:24px}
.fdiv{position:absolute;top:58px;width:1px;height:160px;background:#ccc}
.tw-dot{position:absolute;left:806px;top:44px;width:30px;height:30px;border-radius:50%;background:#222}
.tw h4{padding-left:44px}
.tw p{font-size:13px;line-height:16px;color:#555;width:270px}
.tw .meta{margin-top:18px;font-size:12px;color:#555}
.bottom{position:absolute;left:0;top:2430px;width:1200px;height:42px;background:var(--bottom);color:#fff;font-size:12px}
.bottom .copy{position:absolute;left:127px;top:14px}
.bottom .pay{position:absolute;left:754px;top:14px}
.cards{position:absolute;left:874px;top:9px;display:flex;gap:4px}
.cards span{width:36px;height:24px;background:#f4f4f4;border-radius:2px;color:#234;font-size:9px;font-weight:700;display:flex;align-items:center;justify-content:center}
</style>
</head>
<body>

<header class="masthead">
  <div class="brand">
    <div class="brand-row"><span class="brand-mark"></span><span class="brand-name">Duoglimmer</span></div>
    <div class="brand-tag">A World Group Buy Organisation</div>
  </div>
  <div class="city">
    <div class="city-name">SINGAPORE
      <svg width="17" height="17" viewBox="0 0 17 17"><circle cx="8.5" cy="8.5" r="8.5" fill="#222"/><path d="M4.5 7l4 4 4-4" stroke="#fff" stroke-width="2" fill="none"/></svg>
    </div>
    <div class="city-sub">Exclusive Deals for Youngs</div>
  </div>
  <div class="city-note" role="img" aria-label="Hand-lettered note reading Find Your City Deal with a curved arrow"></div>
  <div class="newsletter">
    <div class="newsletter-title">Duoglimmer Daily Deal Newsletter</div>
    <div class="newsletter-form"><div class="newsletter-input">Enter Your Email ID</div><div class="newsletter-send">SEND</div></div>
  </div>
</header>

<nav class="navbar">
  <div class="nav-main">
    <a style="left:0">HOME</a>
    <a class="active" style="left:80px">CURRENT DEALS</a>
    <a style="left:233px">PAST DEALS</a>
    <a style="left:356px">BLOG</a>
    <a style="left:437px">ABOUT US</a>
  </div>
  <div class="nav-util"><span class="sign-in">SIGN IN</span><span style="margin-left:10px">REGISTER</span><span class="sep"></span><span>FAQ</span></div>
  <span class="social-circle" style="left:1007px"></span>
  <span class="social-circle" style="left:1043px"></span>
</nav>

<div class="wrap breadcrumb">You Are Here:&nbsp; Home &nbsp;›&nbsp; All Deals</div>

<section class="wrap search">
  <div class="field" style="left:17px;width:372px">Enter Keyword</div>
  <div class="field-hint" style="left:20px">Keyword : Restaurantt, food, dinner, lunch cake etc.</div>
  <div class="field" style="left:406px;width:382px">Location</div>
  <div class="field-hint" style="left:406px">Select any one location where you wana find deal :)</div>
  <div class="find-btn">FIND DEALS !</div>
</section>

<h1 class="wrap page-title">Activities</h1>
<p class="wrap page-intro">Showing 1-20 of 149 deals in Washington DC available Today Lorem Ipsum is simply dummy text of the printing and typesetting industry. Lorem Ipsum has been the industry's standard dummy text</p>

<div class="wrap sorter">
  <b>Deals Sorted</b>
  <span class="tab">Best Prices</span>
  <span style="left:241px">Discount</span>
  <span style="left:312px">Time Lefts</span>
  <span style="left:392px">Best Offer Deals</span>
</div>

<main class="wrap deals">
  <article class="deal featured">
    <div class="price-tag"><span class="amount">$39</span><span class="unit">ONLY</span></div>
    <p class="deal-title">Lorem ipsum dolor sit amet, consectetur adipiscing elit. Lorem ipsum dolor sit amet, consectetur adipiscing elit.</p>
    <div class="stats">
      <div class="stat-row"><span class="c1">Value</span><span class="c2">$99</span><span class="c3 orange">Time Left</span><span class="c4 orange">2 days 16:07:39</span></div>
      <div class="stat-row shaded"><span class="c1">Discount</span><span class="c2">76%</span><span class="c3">Deals is on</span><span class="c4">11 Bought!!</span></div>
      <div class="stat-row"><span class="c1">Saving</span><span class="c2">$75</span><span class="c3">Social Icons</span><span class="icons"><i style="background:#3b5998"></i><i style="background:#29a9e1"></i><i style="background:#0e76a8"></i><i style="background:#f26522"></i></span></div>
    </div>
    <span class="btn btn-buy">Buy Now</span><span class="btn btn-details">Details</span>
    <div class="deal-photo" role="img" aria-label="Photo of fresh croissants on a plate" style="background:linear-gradient(135deg,#e8d8c2,#c88a4a 55%,#5a2e1a)"></div>
  </article>

  <article class="deal">
    <div class="price-tag"><span class="amount">$59</span><span class="unit">ONLY</span></div>
    <div class="stats">
      <div class="stat-row"><span class="c1">Value</span><span class="c2">$199</span><span class="c3 orange">Time Left</span><span class="c4 orange">2 days 16:07:39</span></div>
      <div class="stat-row shaded"><span class="c1">Discount</span><span class="c2">76%</span><span class="c3">Deals is on</span><span class="c4">11 Bought!!</span></div>
      <div class="stat-row"><span class="c1">Saving</span><span class="c2">$75</span><span class="c3">Social Icons</span><span class="icons"><i style="background:#3b5998"></i><i style="background:#29a9e1"></i><i style="background:#0e76a8"></i><i style="background:#f26522"></i></span></div>
    </div>
    <span class="btn btn-buy">Buy Now</span><span class="btn btn-details">Details</span>
    <div class="deal-photo" role="img" aria-label="Photo of stacked chocolate brownies" style="background:linear-gradient(135deg,#6b4a34,#3d2618 60%,#7a6a5a)"></div>
  </article>

  <article class="deal">
    <div class="price-tag"><span class="amount">$159</span><span class="unit">ONLY</span></div>
    <p class="deal-title">Lorem ipsum dolor sit amet, consectetur adipiscing elit. Lorem ipsum dolor sit amet, consectetur adipiscing elit.</p>
    <div class="stats">
      <div class="stat-row"><span class="c1">Value</span><span class="c2">$399</span><span class="c3 orange">Time Left</span><span class="c4 orange">2 days 16:07:39</span></div>
      <div class="stat-row shaded"><span class="c1">Discount</span><span class="c2">76%</span><span class="c3">Deals is on</span><span class="c4">11 Bought!!</span></div>
      <div class="stat-row"><span class="c1">Saving</span><span class="c2">$75</span><span class="c3">Social Icons</span><span class="icons"><i style="background:#3b5998"></i><i style="background:#29a9e1"></i><i style="background:#0e76a8"></i><i style="background:#f26522"></i></span></div>
    </div>
    <span class="btn btn-buy">Buy Now</span><span class="btn btn-details">Details</span>
    <div class="deal-photo" role="img" aria-label="Photo of a couple toasting at a candlelit dinner" style="background:linear-gradient(135deg,#3a2a1e,#a8704a 50%,#2a1e16)"></div>
  </article>

  <article class="deal">
    <div class="price-tag"><span class="amount">$359</span><span class="unit">ONLY</span></div>
    <p class="deal-title">Lorem ipsum dolor sit amet, consectetur adipiscing elit. Lorem ipsum dolor sit amet, consectetur adipiscing elit.</p>
    <div class="stats">
      <div class="stat-row"><span class="c1">Value</span><span class="c2">$999</span><span class="c3 orange">Time Left</span><span class="c4 orange">2 days 16:07:39</span></div>
      <div class="stat-row shaded"><span class="c1">Discount</span><span class="c2">76%</span><span class="c3">Deals is on</span><span class="c4">11 Bought!!</span></div>
      <div class="stat-row"><span class="c1">Saving</span><span class="c2">$75</span><span class="c3">Social Icons</span><span class="icons"><i style="background:#3b5998"></i><i style="background:#29a9e1"></i><i style="background:#0e76a8"></i><i style="background:#f26522"></i></span></div>
    </div>
    <span class="btn btn-buy">Buy Now</span><span class="btn btn-details">Details</span>
    <div class="deal-photo" role="img" aria-label="Photo of a tiered stand of colourful desserts" style="background:linear-gradient(135deg,#c9d6de,#8a6a4a 45%,#b03a3a 75%,#e6e0d8)"></div>
  </article>

  <article class="deal">
    <div class="price-tag"><span class="amount">$159</span><span class="unit">ONLY</span></div>
    <p class="deal-title">Lorem ipsum dolor sit amet, consectetur adipiscing elit. Lorem ipsum dolor sit amet, consectetur adipiscing elit.</p>
    <div class="stats">
      <div class="stat-row"><span class="c1">Value</span><span class="c2">$599</span><span class="c3 orange">Time Left</span><span class="c4 orange">2 days 16:07:39</span></div>
      <div class="stat-row shaded"><span class="c1">Discount</span><span class="c2">76%</span><span class="c3">Deals is on</span><span class="c4">11 Bought!!</span></div>
      <div class="stat-row"><span class="c1">Saving</span><span class="c2">$75</span><span class="c3">Social Icons</span><span class="icons"><i style="background:#3b5998"></i><i style="background:#29a9e1"></i><i style="background:#0e76a8"></i><i style="background:#f26522"></i></span></div>
    </div>
    <span class="btn btn-buy">Buy Now</span><span class="btn btn-details">Details</span>
    <div class="deal-photo" role="img" aria-label="Photo of a couple toasting at a candlelit dinner" style="background:linear-gradient(135deg,#3a2a1e,#a8704a 50%,#2a1e16)"></div>
  </article>

  <article class="deal">
    <div class="price-tag"><span class="amount">$59</span><span class="unit">ONLY</span></div>
    <p class="deal-title">Lorem ipsum dolor sit amet, consectetur adipiscing elit. Lorem ipsum dolor sit amet, consectetur adipiscing elit.</p>
    <div class="stats">
      <div class="stat-row"><span class="c1">Value</span><span class="c2">$199</span><span class="c3 orange">Time Left</span><span class="c4 orange">2 days 16:07:39</span></div>
      <div class="stat-row shaded"><span class="c1">Discount</span><span class="c2">76%</span><span class="c3">Deals is on</span><span class="c4">11 Bought!!</span></div>
      <div class="stat-row"><span class="c1">Saving</span><span class="c2">$75</span><span class="c3">Social Icons</span><span class="icons"><i style="background:#3b5998"></i><i style="background:#29a9e1"></i><i style="background:#0e76a8"></i><i style="background:#f26522"></i></span></div>
    </div>
    <span class="btn btn-buy">Buy Now</span><span class="btn btn-details">Details</span>
    <div class="deal-photo" role="img" aria-label="Photo of stacked chocolate brownies" style="background:linear-gradient(135deg,#6b4a34,#3d2618 60%,#7a6a5a)"></div>
  </article>
</main>

<aside>
  <section class="side categories">
    <div class="widget-head">Deals Categories<small>View all</small></div>
    <ul>
      <li>All Deals</li><li>Local Food &amp; Drink</li><li class="current">Activities</li><li>Health &amp; Beauty</li>
      <li>Health &amp; Beauty</li><li>Shopping</li><li>Home &amp; Auto</li><li>Health &amp; Fitness</li>
      <li>Health &amp; Fitness</li><li>Gift Ideas</li><li>Services</li><li>Home Appliances</li><li>Kids &amp; Toys</li>
    </ul>
  </section>

  <section class="side fan-box">
    <div class="widget-head">Friendwall</div>
    <div class="fan-head">
      <div class="fan-mark"></div>
      <div><div class="fan-name">Duoglimmer <span>on friendwall</span></div><div class="like">Like</div></div>
    </div>
    <div class="fan-count">58,151 people like Duoglimmer</div>
    <div class="fans">
      <div class="fan"><div role="img" aria-label="Member photo" style="background:#8fb0c8"></div>Arvena</div>
      <div class="fan"><div role="img" aria-label="Member photo" style="background:#b89070"></div>Mirelle</div>
      <div class="fan"><div role="img" aria-label="Member photo" style="background:#7a5a4a"></div>Neralie</div>
      <div class="fan"><div role="img" aria-label="Member photo" style="background:#6a5a8a"></div>Ember</div>
      <div class="fan"><div role="img" aria-label="Member photo" style="background:#c8a890"></div>Loma</div>
      <div class="fan"><div role="img" aria-label="Member photo" style="background:#c070b0"></div>Tavin</div>
      <div class="fan"><div role="img" aria-label="Member photo" style="background:#d8dde2"></div>Bevra</div>
      <div class="fan"><div role="img" aria-label="Member photo" style="background:#b0a090"></div>Dorin</div>
    </div>
  </section>

  <section class="side about">
    <h3>About Duoglimmer</h3>
    <p>Lorem ipsum dolor sit amet, consectetur adipiscing elit. Phasellus et est velit, eget viverra lectus. Pellentesque vitae lacinia odio. Curabitur leo augue, auctor quis commodo eu, faucibus eget tellus. Sed nisi sapien, malesuada sed ullamcorper quis, molestie sed elit.</p>
  </section>
</aside>

<footer class="footer">
  <div class="fcol" style="left:129px"><h4>Company</h4><a>Home</a><a>About Us</a><a>Reviews</a><a>Career</a><a>FAQ</a><a>Terms of Use</a></div>
  <span class="fdiv" style="left:279px"></span>
  <div class="fcol" style="left:324px"><h4>Duoglimmer General</h4><a>Suggest a Business</a><a>Business Owners</a><a>Get Featured</a></div>
  <span class="fdiv" style="left:515px"></span>
  <div class="fcol" style="left:560px"><h4>Duoglimmer Support</h4><a>Contact Us</a><a>Help</a><a>Friendwall</a><a>Chirper</a></div>
  <span class="fdiv" style="left:761px"></span>
  <span class="tw-dot"></span>
  <div class="fcol tw" style="left:806px"><h4>Chirper Duoglimmer</h4>
    <p>Lorem ipsum dolor sit amet, consectetur adipiscing elit. Phasellus et est velit, eget viverra lectus. Pellentesque vitae lacinia odio. Curabitur leo augue, auctor quis commodo eu, faucibus eget tellus.</p>
    <div class="meta">http://dg.lk/r8Kq2vn &nbsp;| &nbsp;2hour ago</div>
  </div>
</footer>

<div class="bottom">
  <span class="copy">All right reseved with Duoglimmer © copyright 2012</span>
  <span class="pay">Payment Options</span>
  <div class="cards"><span>Cirlo</span><span>Velpay</span><span>Velpay</span><span>Norvia</span><span>Paxo</span></div>
</div>

</body>
</html>
```